Power point for Phd defence - surgical science

Create a powerpoint for my Phd thesis defence at Brellmoor University. It's scientific presentation of 4 trials I have conducted. 40 minutes, approx. 50 slides. Should consist of 1. Welcome, 2. Background, 3. Presentation of study 1-4 (methods, results, limitations), 4. Discussion, 5. Perspectives, 6. Conclusions
I'd like a nice template where I can add the scientific content which can later be revised.
Deadline November 6.

Target Market(s)

Medical doctors / Surgeons / Professors / Family

Industry/Entity Type

Surgery

Colors

Designer to choose only greyscale colors for use in the design.

Requirements
Must have
• Brellmoor university logo
Nice to have
• I want a nice balance between scientific content and information that can be understood by my family and friends. I'd it to be professional but still light and easy to follow.

```html
<!DOCTYPE html>
<html lang="en">
<head>
<meta charset="utf-8">
<title>PhD defence – surgical science – slide overview</title>
<link href="https://fonts.googleapis.com/css2?family=Open+Sans:wght@400;600;700&display=swap" rel="stylesheet">
<style>
:root{
  --canvas:#ffffff;
  --paper:#ffffff;
  --ink:#3a3a3a;
  --panel:#353535;
  --muted:#8a8a8a;
  --soft:#b5b5b5;
  --line:#d6d6d6;
  --ring:#e6e6e6;
  --accent:#9e1b22;
  --photo-light:#a8a8a8;
  --photo-dark:#4a4a4a;
}
*{box-sizing:border-box;margin:0;padding:0}
html,body{width:1200px;height:1200px;overflow:hidden;background:var(--canvas)}
body{position:relative;font-family:"Open Sans",Arial,sans-serif;color:var(--ink)}

.slide{position:absolute;width:258px;height:145px;background:var(--paper);overflow:hidden;box-shadow:3px 5px 10px rgba(0,0,0,.2)}
.slide.dark{background:var(--panel)}
.c1{left:39px}.c2{left:327px}.c3{left:614px}.c4{left:902px}
.r1{top:71px}.r2{top:253px}.r3{top:435px}.r4{top:618px}.r5{top:800px}.r6{top:982px}

.abs{position:absolute}
.panel{position:absolute;top:0;left:0;height:145px;background:var(--panel)}
.photo{position:absolute;background:linear-gradient(135deg,var(--photo-light),var(--photo-dark))}
.photo.alt{background:linear-gradient(200deg,#c4c4c4,#5c5c5c 70%,#3c3c3c)}
.photo.deep{background:linear-gradient(160deg,#8e8e8e,#2f2f2f)}
.photo.scrubs{background:linear-gradient(150deg,#dfe3e4 0%,#6e8f95 45%,#1f6b70 100%)}

.logo{position:absolute;top:9px;display:flex;align-items:center;gap:2px;font-size:2.6px;font-weight:600;letter-spacing:.35px;text-transform:uppercase;color:#7a7a7a;line-height:1.1}
.logo i{display:block;width:5px;height:5px;border-radius:50%;background:var(--accent)}
.logo.right{left:206px}.logo.left{left:19px}
.logo.onDark{color:#cfcfcf}

.title{position:absolute;font-weight:700;color:var(--ink);line-height:1.08}
.title.light{color:#fff}
.title.center{text-align:center}
.title.end{text-align:right}
.t9{font-size:9px}.t8{font-size:8px}.t75{font-size:7.5px}

.rule{position:absolute;height:0;border-top:.5px solid var(--line)}
.rule::after{content:"";position:absolute;left:8px;top:-2px;width:3.5px;height:3.5px;border-radius:50%;background:var(--soft)}
.rule.onDark{border-color:#5a5a5a}

.para{position:absolute;font-size:2.5px;line-height:1.55;color:#808080;text-align:justify}
.para.light{color:#bdbdbd}
.para.center{text-align:center}

.foot{position:absolute;bottom:5px;font-size:2.3px;color:#aaa;white-space:nowrap}
.foot.date{left:19px}.foot.uni{left:86px}.foot.num{right:20px}

/* title slide */
.seal{position:absolute;left:29px;top:28px;width:91px;height:91px;border-radius:50%;background:var(--ring);display:flex;align-items:center;justify-content:center}
.seal-core{width:75px;height:75px;border-radius:50%;background:var(--panel);display:flex;flex-direction:column;align-items:center;justify-content:center;gap:4px}
.seal-core i{width:7px;height:7px;border-radius:50%;background:var(--accent)}
.seal-name{font-size:3.6px;letter-spacing:.6px;text-transform:uppercase;color:#a8a8a8;text-align:center;line-height:1.3}
.cover-title{position:absolute;left:139px;top:47px;font-size:11px;line-height:1.07;color:#444}
.cover-title b{font-weight:700}
.cover-title span{font-weight:400}
.presenter{position:absolute;left:139px;top:104px;font-size:2.8px;color:#777;text-transform:uppercase}

/* contents */
.toc-item{position:absolute;display:flex;align-items:flex-start;gap:4px}
.toc-num{width:11px;height:11px;border-radius:50%;border:1.2px solid #dedede;font-size:3.6px;font-weight:600;display:flex;align-items:center;justify-content:center;color:#555;flex:none}
.toc-text b{display:block;font-size:4.6px;font-weight:600;color:#444;margin-top:1px}
.toc-text small{display:block;font-size:2.2px;color:#999}

/* intro circle */
.intro-badge{position:absolute;left:170px;top:45px;width:56px;height:56px;border-radius:50%;background:rgba(255,255,255,.18);display:flex;align-items:center;justify-content:center;font-size:5.5px;color:#fff}

/* lists */
.bullets{position:absolute;list-style:none;font-size:2.5px;line-height:1.55;color:#d0d0d0}
.bullets li::before{content:"";display:inline-block;width:1.6px;height:1.6px;border-radius:50%;background:#fff;margin-right:2px;vertical-align:middle}
.bullets.dark{color:#8a8a8a}
.bullets.dark li::before{background:#555}
.bullet-text{position:absolute;font-size:2.5px;line-height:1.55;color:#d0d0d0;text-align:justify;padding-left:3px}
.bullet-text::before{content:"";position:absolute;left:0;top:1.4px;width:1.6px;height:1.6px;border-radius:50%;background:#fff}

.item{position:absolute}
.item h3{font-size:4.2px;font-weight:700;color:#444;margin-bottom:2px}
.item p{font-size:2.4px;line-height:1.55;color:#888;text-align:justify}

.subtitle{position:absolute;font-size:4.5px;color:#999}
.greeting{position:absolute;font-size:4px;font-weight:700;color:#333;line-height:1.2}

/* timeline */
.year{position:absolute;left:98px;width:17px;height:6px;background:var(--panel);color:#fff;font-size:3px;font-weight:700;display:flex;align-items:center;justify-content:center}
.year::after{content:"";position:absolute;left:17px;top:3px;width:12px;border-top:.5px solid var(--line)}
.vline{position:absolute;width:0;border-left:.5px solid var(--line)}
.node{position:absolute;left:127px;width:2.5px;height:2.5px;border-radius:50%;background:var(--soft)}

/* captions */
.caption{position:absolute;font-size:3.7px;font-weight:600;color:#444;text-align:center}
.info-box{position:absolute;background:var(--panel);padding:6px}
.info-box h4{font-size:3.8px;font-weight:600;color:#fff;margin-bottom:2px}
.info-box p{font-size:2.3px;line-height:1.5;color:#cfcfcf}
.info-box.end{text-align:right}
</style>
</head>
<body>

<!-- 1 Cover -->
<section class="slide c1 r1">
  <div class="seal"><div class="seal-core"><i></i><span class="seal-name">Brellmoor<br>University</span></div></div>
  <h1 class="cover-title"><b>Phd defence -<br>surgical science</b><br><span>Brellmoor<br>University.</span></h1>
  <div class="rule" style="left:139px;top:98px;width:90px"></div>
  <p class="presenter">Peter Anders Holm</p>
  <span class="foot uni">Brellmoor University - Phd defence - surgical science</span>
</section>

<!-- 2 Welcome -->
<section class="slide c2 r1">
  <div class="logo right"><i></i><span>Brellmoor<br>University</span></div>
  <h2 class="title center t9" style="left:0;right:0;top:58px">Welcome to My presentation!</h2>
  <p class="para center" style="left:46px;top:73px;width:166px">Short placeholder text describes the study background, the chosen methods and the main clinical findings, written so that colleagues and family can follow each step. Add results, limitations and notes here once the trial data is final.</p>
  <span class="foot uni">Brellmoor University - Phd defence - surgical science</span>
  <span class="foot num">2</span>
</section>

<!-- 3 Before starting -->
<section class="slide dark c3 r1">
  <div class="logo left onDark"><i></i><span>Brellmoor<br>University</span></div>
  <h2 class="title light t9" style="left:44px;top:61px">Before<br>starting</h2>
  <div class="rule onDark" style="left:44px;top:85px;width:44px"></div>
  <p class="bullet-text" style="left:118px;top:22px;width:98px">Short placeholder text describes the study background, the chosen methods and the main clinical findings, written so that colleagues and family can follow each step. Short placeholder text describes the study background, the chosen methods and the main clinical findings, written so that colleagues and family can follow each step.</p>
  <p class="bullet-text" style="left:118px;top:82px;width:98px">Short placeholder text describes the study background, the chosen methods and the main clinical findings, written so that colleagues and family can follow each step. Add results, limitations and notes here once the trial data is final.</p>
  <span class="foot date" style="color:#777">Thursday, October 5, 2023</span>
  <span class="foot uni" style="color:#777">Brellmoor University - Phd defence - surgical science</span>
</section>

<!-- 4 Contents grid -->
<section class="slide c4 r1">
  <div class="panel" style="width:92px"></div>
  <div class="logo right"><i></i><span>Brellmoor<br>University</span></div>
  <h2 class="title light t9" style="left:24px;top:67px">Contents</h2>
  <div class="rule onDark" style="left:24px;top:81px;width:68px"></div>
  <div class="toc-item" style="left:108px;top:44px"><span class="toc-num">1</span><div class="toc-text"><b>Introduction</b><small>Before starting</small></div></div>
  <div class="toc-item" style="left:108px;top:67px"><span class="toc-num">2</span><div class="toc-text"><b>About us</b><small>What we did, what we do</small></div></div>
  <div class="toc-item" style="left:108px;top:89px"><span class="toc-num">3</span><div class="toc-text"><b>Our portfolio</b><small>Our amazing products</small></div></div>
  <div class="toc-item" style="left:176px;top:44px"><span class="toc-num">4</span><div class="toc-text"><b>New proposal</b><small>Our awesome ideas</small></div></div>
  <div class="toc-item" style="left:176px;top:67px"><span class="toc-num">5</span><div class="toc-text"><b>Analysis</b><small>Marketing data and our estimation</small></div></div>
  <div class="toc-item" style="left:176px;top:89px"><span class="toc-num">6</span><div class="toc-text"><b>Contact us</b><small>Get in touch</small></div></div>
  <span class="foot date" style="color:#777">Thursday, October 5, 2023</span>
  <span class="foot uni">Brellmoor University - Phd defence - surgical science</span>
  <span class="foot num">4</span>
</section>

<!-- 5 Contents list -->
<section class="slide c1 r2">
  <div class="panel" style="width:92px"></div>
  <div class="logo right"><i></i><span>Brellmoor<br>University</span></div>
  <h2 class="title light t9" style="left:24px;top:67px">Contents</h2>
  <div class="rule onDark" style="left:24px;top:81px;width:68px"></div>
  <div class="toc-item" style="left:129px;top:22px"><span class="toc-num">1</span><div class="toc-text"><b>Introduction</b><small>Before starting</small></div></div>
  <div class="toc-item" style="left:129px;top:45px"><span class="toc-num">2</span><div class="toc-text"><b>About us</b><small>What we did, what we do</small></div></div>
  <div class="toc-item" style="left:129px;top:67px"><span class="toc-num">3</span><div class="toc-text"><b>Our portfolio</b><small>Our amazing products</small></div></div>
  <div class="toc-item" style="left:129px;top:90px"><span class="toc-num">4</span><div class="toc-text"><b>New proposal</b><small>Our awesome ideas</small></div></div>
  <div class="toc-item" style="left:129px;top:112px"><span class="toc-num">5</span><div class="toc-text"><b>Analysis</b><small>Marketing data and our estimation</small></div></div>
  <span class="foot date" style="color:#777">Thursday, October 5, 2023</span>
  <span class="foot uni">Brellmoor University - Phd defence - surgical science</span>
  <span class="foot num">5</span>
</section>

<!-- 6 Introduction divider -->
<section class="slide c2 r2">
  <div class="photo deep" style="left:0;top:0;width:258px;height:145px" role="img" aria-label="Black and white photo of surgeons in an operating room, one holding a tablet"></div>
  <div class="logo left onDark"><i></i><span>Brellmoor<br>University</span></div>
  <div class="intro-badge">Introduction</div>
</section>

<!-- 7 Introduction -->
<section class="slide c3 r2">
  <div class="photo alt" style="left:0;top:0;width:258px;height:99px" role="img" aria-label="Black and white close-up of gloved hands holding a surgical instrument"></div>
  <div class="logo left onDark"><i></i><span>Brellmoor<br>University</span></div>
  <h2 class="title t9" style="left:21px;top:107px">Introduction</h2>
  <div class="rule" style="left:21px;top:120px;width:55px"></div>
  <p class="para" style="left:92px;top:104px;width:150px">Short placeholder text describes the study background, the chosen methods and the main clinical findings, written so that colleagues and family can follow each step. Add results, limitations and notes here once the trial data is final.</p>
  <span class="foot date">Thursday, October 5, 2023</span>
  <span class="foot uni">Brellmoor University - Phd defence - surgical science</span>
  <span class="foot num">7</span>
</section>

<!-- 8 Presenter dark -->
<section class="slide dark c4 r2">
  <div class="photo deep" style="left:20px;top:0;width:80px;height:145px" role="img" aria-label="Black and white portrait of a surgeon wearing loupes and a mask"></div>
  <div class="logo right onDark"><i></i><span>Brellmoor<br>University</span></div>
  <h2 class="title light t8" style="left:130px;top:38px;font-weight:600">PETER ANDERS HOLM</h2>
  <p class="subtitle" style="left:130px;top:49px;color:#ddd;font-size:3.8px">surgical science</p>
  <div class="rule onDark" style="left:130px;top:59px;width:112px"></div>
  <p class="para light" style="left:130px;top:64px;width:112px">Short placeholder text describes the study background, the chosen methods and the main clinical findings, written so that colleagues and family can follow each step. Add results, limitations and notes here once the trial data is final.</p>
  <ul class="bullets" style="left:130px;top:111px"><li>Profile page</li><li>Research page</li><li>Contact page</li></ul>
  <span class="foot date" style="color:#777">Thursday, October 5, 2023</span>
  <span class="foot uni" style="color:#777">Brellmoor University - Phd defence - surgical science</span>
</section>

<!-- 9 Presenter light -->
<section class="slide c1 r3">
  <div class="logo left"><i></i><span>Brellmoor<br>University</span></div>
  <h2 class="title t8" style="left:21px;top:39px;font-weight:600">PETER ANDERS HOLM</h2>
  <p class="subtitle" style="left:21px;top:51px">surgical science</p>
  <div class="rule" style="left:21px;top:63px;width:90px"></div>
  <p class="greeting" style="left:21px;top:68px">Hello, everyone!<br>Let me introduce myself a bit.</p>
  <p class="para" style="left:21px;top:80px;width:100px">Short placeholder text describes the study background, the chosen methods and the main clinical findings, written so that colleagues and family can follow each step. Add results, limitations and notes here once the trial data is final.</p>
  <div class="photo scrubs" style="left:158px;top:0;width:80px;height:145px" role="img" aria-label="Photo of a surgeon in teal scrubs, cap and loupes"></div>
  <span class="foot date">Thursday, October 5, 2023</span>
  <span class="foot uni">Brellmoor University - Phd defence - surgical science</span>
</section>

<!-- 10 Study background -->
<section class="slide c2 r3">
  <div class="panel" style="width:129px"></div>
  <div class="logo right"><i></i><span>Brellmoor<br>University</span></div>
  <h2 class="title light center t9" style="left:0;width:129px;top:56px">Surgical Science<br>Study<br>Background</h2>
  <h2 class="title t75" style="left:142px;top:33px;font-weight:600">Surgical Science<br>Study Background</h2>
  <div class="rule" style="left:142px;top:54px;width:100px"></div>
  <p class="para" style="left:142px;top:58px;width:104px">Short placeholder text describes the study background, the chosen methods and the main clinical findings, written so that colleagues and family can follow each step. Short placeholder text describes the study background, the chosen methods and the main clinical findings, written so that colleagues and family can follow each step. Add results, limitations and notes here once the trial data is final.</p>
  <span class="foot date" style="color:#777">Thursday, October 5, 2023</span>
  <span class="foot uni">Brellmoor University - Phd defence - surgical science</span>
  <span class="foot num">10</span>
</section>

<!-- 11 Study methods -->
<section class="slide c3 r3">
  <div class="vline" style="left:114px;top:0;height:145px"></div>
  <div class="logo right"><i></i><span>Brellmoor<br>University</span></div>
  <h2 class="title end t8" style="right:149px;top:52px;font-weight:600">#1<br>Study methods,</h2>
  <div class="photo alt" style="left:117px;top:40px;width:141px;height:36px" role="img" aria-label="Black and white photo of gloved hands during surgery"></div>
  <p class="para" style="left:117px;top:81px;width:115px">Short placeholder text describes the study background, the chosen methods and the main clinical findings, written so that colleagues and family can follow each step.</p>
  <span class="foot date">Thursday, October 5, 2023</span>
  <span class="foot uni">Brellmoor University - Phd defence - surgical science</span>
  <span class="foot num">11</span>
</section>

<!-- 12 Study methods list -->
<section class="slide c4 r3">
  <div class="logo left"><i></i><span>Brellmoor<br>University</span></div>
  <h2 class="title t9" style="left:21px;top:57px">#1<br>Study<br>methods</h2>
  <div class="rule" style="left:21px;top:91px;width:50px"></div>
  <div class="photo alt" style="left:77px;top:0;width:80px;height:145px" role="img" aria-label="Black and white photo of gloved hands holding surgical instruments"></div>
  <div class="item" style="left:159px;top:20px;width:82px"><h3>Simply dummy text</h3><p>Add results, limitations and notes here once the trial data is final.</p></div>
  <div class="item" style="left:159px;top:58px;width:82px"><h3>Simply dummy text</h3><p>Add results, limitations and notes here once the trial data is final.</p></div>
  <div class="item" style="left:159px;top:96px;width:82px"><h3>Simply dummy text</h3><p>Add results, limitations and notes here once the trial data is final.</p></div>
  <span class="foot date">Thursday, October 5, 2023</span>
  <span class="foot num">12</span>
</section>

<!-- 13 Method background -->
<section class="slide c1 r4">
  <div class="logo left"><i></i><span>Brellmoor<br>University</span></div>
  <h2 class="title t9" style="left:21px;top:37px">Surgical Science<br>Study method<br>Background</h2>
  <div class="rule" style="left:21px;top:71px;width:120px"></div>
  <p class="para" style="left:21px;top:77px;width:130px">Short placeholder text describes the study background, the chosen methods and the main clinical findings, written so that colleagues and family can follow each step. Short placeholder text describes the study background, the chosen methods and the main clinical findings, written so that colleagues and family can follow each step. Add results, limitations and notes here once the trial data is final.</p>
  <div class="photo alt" style="left:158px;top:0;width:80px;height:145px" role="img" aria-label="Black and white photo of gloved hands placing an oxygen mask on a patient"></div>
  <span class="foot date">Thursday, October 5, 2023</span>
  <span class="foot uni">Brellmoor University - Phd defence - surgical science</span>
  <span class="foot num">13</span>
</section>

<!-- 14 Timeline with title -->
<section class="slide c2 r4">
  <div class="logo left"><i></i><span>Brellmoor<br>University</span></div>
  <h2 class="title t8" style="left:21px;top:32px;font-weight:600">Surgical<br>Science<br>Study method<br>Timeline</h2>
  <p class="para" style="left:21px;top:77px;width:66px">Short placeholder text describes the study background, the chosen methods and the main clinical findings, written so that colleagues and family can follow each step. Add results, limitations and notes here once the trial data is final.</p>
  <div class="vline" style="left:128px;top:30px;height:95px"></div>
  <span class="year" style="top:36px">2010</span><span class="node" style="top:38px"></span>
  <span class="year" style="top:70px">2012</span><span class="node" style="top:72px"></span>
  <span class="year" style="top:103px">2014</span><span class="node" style="top:105px"></span>
  <div class="item" style="left:137px;top:35px;width:80px"><h3>Dummy text</h3><p>Short note on this year's milestone and what changed in the trial.</p></div>
  <div class="item" style="left:137px;top:69px;width:80px"><h3>Dummy text</h3><p>Short note on this year's milestone and what changed in the trial.</p></div>
  <div class="item" style="left:137px;top:102px;width:80px"><h3>Dummy text</h3><p>Short note on this year's milestone and what changed in the trial.</p></div>
  <span class="foot date">Thursday, October 5, 2023</span>
  <span class="foot uni">Brellmoor University - Phd defence - surgical science</span>
  <span class="foot num">15</span>
</section>

<!-- 15 Timeline plain -->
<section class="slide c3 r4">
  <div class="logo left"><i></i><span>Brellmoor<br>University</span></div>
  <div class="vline" style="left:128px;top:0;height:140px"></div>
  <span class="year" style="top:36px">2010</span><span class="node" style="top:38px"></span>
  <span class="year" style="top:70px">2012</span><span class="node" style="top:72px"></span>
  <span class="year" style="top:103px">2014</span><span class="node" style="top:105px"></span>
  <div class="item" style="left:137px;top:35px;width:80px"><h3>Dummy text</h3><p>Short note on this year's milestone and what changed in the trial.</p></div>
  <div class="item" style="left:137px;top:69px;width:80px"><h3>Dummy text</h3><p>Short note on this year's milestone and what changed in the trial.</p></div>
  <div class="item" style="left:137px;top:102px;width:80px"><h3>Dummy text</h3><p>Short note on this year's milestone and what changed in the trial.</p></div>
  <span class="foot date">Thursday, October 5, 2023</span>
  <span class="foot uni">Brellmoor University - Phd defence - surgical science</span>
  <span class="foot num">16</span>
</section>

<!-- 16 Timeline stacked title -->
<section class="slide c4 r4">
  <div class="logo left"><i></i><span>Brellmoor<br>University</span></div>
  <h2 class="title t8" style="left:21px;top:49px;font-weight:600">Surgical<br>Science<br>Study<br>method<br>Timeline</h2>
  <div class="rule" style="left:21px;top:100px;width:50px"></div>
  <div class="vline" style="left:128px;top:30px;height:95px"></div>
  <span class="year" style="top:36px">2016</span><span class="node" style="top:38px"></span>
  <span class="year" style="top:70px">2018</span><span class="node" style="top:72px"></span>
  <span class="year" style="top:103px">2020</span><span class="node" style="top:105px"></span>
  <div class="item" style="left:137px;top:35px;width:80px"><h3>Dummy text</h3><p>Short note on this year's milestone and what changed in the trial.</p></div>
  <div class="item" style="left:137px;top:69px;width:80px"><h3>Dummy text</h3><p>Short note on this year's milestone and what changed in the trial.</p></div>
  <div class="item" style="left:137px;top:102px;width:80px"><h3>Dummy text</h3><p>Short note on this year's milestone and what changed in the trial.</p></div>
  <span class="foot date">Thursday, October 5, 2023</span>
  <span class="foot uni">Brellmoor University - Phd defence - surgical science</span>
  <span class="foot num">17</span>
</section>

<!-- 17 Method background photo left -->
<section class="slide c1 r5">
  <div class="photo deep" style="left:20px;top:0;width:80px;height:145px" role="img" aria-label="Black and white photo of a surgeon in cap and mask operating"></div>
  <div class="logo right"><i></i><span>Brellmoor<br>University</span></div>
  <h2 class="title t8" style="left:127px;top:38px;font-weight:600">Surgical Science<br>Study method<br>Background</h2>
  <div class="rule" style="left:127px;top:71px;width:112px"></div>
  <p class="para" style="left:127px;top:76px;width:115px">Short placeholder text describes the study background, the chosen methods and the main clinical findings, written so that colleagues and family can follow each step. Add results, limitations and notes here once the trial data is final.</p>
  <span class="foot date" style="color:#eee">Thursday, October 5, 2023</span>
  <span class="foot uni">Brellmoor University - Phd defence - surgical science</span>
  <span class="foot num">14</span>
</section>

<!-- 18 Method background list -->
<section class="slide c2 r5">
  <div class="panel" style="width:92px"></div>
  <div class="logo right"><i></i><span>Brellmoor<br>University</span></div>
  <h2 class="title light t8" style="left:19px;top:57px;font-weight:600">Surgical<br>Science<br>Study method<br>Background</h2>
  <div class="rule onDark" style="left:19px;top:95px;width:73px"></div>
  <div class="item" style="left:130px;top:20px;width:88px"><h3>Dummy text</h3><p>Short placeholder text describes the study background, the chosen methods and the main clinical findings, written so that colleagues and family can follow each step.</p></div>
  <div class="item" style="left:130px;top:58px;width:88px"><h3>Dummy text</h3><p>Short placeholder text describes the study background, the chosen methods and the main clinical findings, written so that colleagues and family can follow each step.</p></div>
  <div class="item" style="left:130px;top:96px;width:88px"><h3>Dummy text</h3><p>Short placeholder text describes the study background, the chosen methods and the main clinical findings, written so that colleagues and family can follow each step.</p></div>
  <span class="foot date" style="color:#777">Thursday, October 5, 2023</span>
  <span class="foot uni">Brellmoor University - Phd defence - surgical science</span>
  <span class="foot num">18</span>
</section>

<!-- 19 Method background photo -->
<section class="slide c3 r5">
  <div class="panel" style="width:92px"></div>
  <div class="logo right"><i></i><span>Brellmoor<br>University</span></div>
  <h2 class="title light t8" style="left:19px;top:57px;font-weight:600">Surgical<br>Science<br>Study method<br>Background</h2>
  <div class="rule onDark" style="left:19px;top:95px;width:73px"></div>
  <div class="photo alt" style="left:112px;top:24px;width:127px;height:52px" role="img" aria-label="Black and white photo of gloved hands holding a surgical instrument"></div>
  <p class="para" style="left:112px;top:81px;width:127px">Short placeholder text describes the study background, the chosen methods and the main clinical findings, written so that colleagues and family can follow each step. Short placeholder text describes the study background, the chosen methods and the main clinical findings, written so that colleagues and family can follow each step.</p>
  <span class="foot date" style="color:#777">Thursday, October 5, 2023</span>
  <span class="foot uni">Brellmoor University - Phd defence - surgical science</span>
  <span class="foot num">19</span>
</section>

<!-- 20 Three methods -->
<section class="slide c4 r5">
  <div class="logo right"><i></i><span>Brellmoor<br>University</span></div>
  <div class="photo deep" style="left:20px;top:35px;width:72px;height:37px" role="img" aria-label="Black and white photo of a surgical team in theatre"></div>
  <div class="photo alt" style="left:94px;top:35px;width:71px;height:37px" role="img" aria-label="Black and white photo of surgeons operating"></div>
  <div class="photo deep" style="left:167px;top:35px;width:71px;height:37px" role="img" aria-label="Black and white photo of a surgeon at the operating table"></div>
  <p class="caption" style="left:20px;top:75px;width:72px">Surgical method #1</p>
  <p class="caption" style="left:94px;top:75px;width:71px">Surgical method #2</p>
  <p class="caption" style="left:167px;top:75px;width:71px">Surgical method #3</p>
  <h2 class="title end t8" style="right:158px;top:88px;font-weight:600">Surgical Science<br>Study method<br>Background</h2>
  <div class="rule" style="left:21px;top:123px;width:80px"></div>
  <p class="para" style="left:110px;top:90px;width:128px">Short placeholder text describes the study background, the chosen methods and the main clinical findings, written so that colleagues and family can follow each step. Add results, limitations and notes here once the trial data is final.</p>
  <span class="foot date">Thursday, October 5, 2023</span>
  <span class="foot uni">Brellmoor University - Phd defence - surgical science</span>
  <span class="foot num">20</span>
</section>

<!-- 21 Gallery grid -->
<section class="slide c1 r6">
  <div class="logo right"><i></i><span>Brellmoor<br>University</span></div>
  <div class="photo alt" style="left:20px;top:20px;width:59px;height:51px" role="img" aria-label="Black and white photo of surgeons over a patient"></div>
  <div class="photo deep" style="left:20px;top:73px;width:59px;height:52px" role="img" aria-label="Black and white photo of a surgeon wearing loupes"></div>
  <div class="photo alt" style="left:81px;top:20px;width:48px;height:105px" role="img" aria-label="Black and white photo of a surgeon operating"></div>
  <h2 class="title t8" style="left:159px;top:32px;font-weight:600">Surgical<br>Science<br>Study method<br>Gallery</h2>
  <div class="rule" style="left:159px;top:72px;width:80px"></div>
  <p class="para" style="left:159px;top:77px;width:80px">Short placeholder text describes the study background, the chosen methods and the main clinical findings, written so that colleagues and family can follow each step. Add results, limitations and notes here once the trial data is final.</p>
  <span class="foot date">Thursday, October 5, 2023</span>
  <span class="foot uni">Brellmoor University - Phd defence - surgical science</span>
  <span class="foot num">21</span>
</section>

<!-- 22 Gallery with boxes -->
<section class="slide c2 r6">
  <div class="logo left"><i></i><span>Brellmoor<br>University</span></div>
  <h2 class="title t8" style="left:21px;top:52px;font-weight:600">Surgical<br>Science<br>Study<br>method<br>Gallery</h2>
  <div class="rule" style="left:21px;top:103px;width:60px"></div>
  <div class="photo alt" style="left:92px;top:0;width:73px;height:72px" role="img" aria-label="Black and white photo of surgeons operating"></div>
  <div class="info-box" style="left:165px;top:0;width:73px;height:72px;padding-top:16px"><h4>Surgical method #1</h4><p>Add results, limitations and notes here once the trial data is final.</p></div>
  <div class="info-box end" style="left:92px;top:72px;width:73px;height:73px;padding-top:16px"><h4>Surgical method #2</h4><p>Add results, limitations and notes here once the trial data is final.</p></div>
  <div class="photo deep" style="left:165px;top:72px;width:73px;height:73px" role="img" aria-label="Black and white photo of a surgeon with loupes"></div>
  <span class="foot date">Thursday, October 5, 2023</span>
</section>

<!-- 23 Gallery collage -->
<section class="slide c3 r6">
  <div class="logo right"><i></i><span>Brellmoor<br>University</span></div>
  <h2 class="title t8" style="left:21px;top:31px;font-weight:600">Surgical<br>Science<br>Study method<br>Gallery</h2>
  <div class="rule" style="left:21px;top:70px;width:105px"></div>
  <p class="para" style="left:21px;top:74px;width:115px">Short placeholder text describes the study background, the chosen methods and the main clinical findings, written so that colleagues and family can follow each step. Add results, limitations and notes here once the trial data is final.</p>
  <div class="photo alt" style="left:125px;top:20px;width:59px;height:54px" role="img" aria-label="Black and white photo of a surgical team"></div>
  <div class="photo deep" style="left:184px;top:40px;width:38px;height:44px" role="img" aria-label="Black and white photo of surgeons at work"></div>
  <div class="photo alt" style="left:144px;top:76px;width:46px;height:35px" role="img" aria-label="Black and white close-up of surgical hands"></div>
  <div class="photo deep" style="left:191px;top:84px;width:45px;height:41px" role="img" aria-label="Black and white photo of a surgeon operating"></div>
  <span class="foot date">Thursday, October 5, 2023</span>
  <span class="foot uni">Brellmoor University - Phd defence - surgical science</span>
  <span class="foot num">23</span>
</section>

<!-- 24 Single method -->
<section class="slide c4 r6">
  <div class="logo left"><i></i><span>Brellmoor<br>University</span></div>
  <h2 class="title t8" style="left:21px;top:33px;font-weight:600">Surgical<br>Science<br>Study<br>method</h2>
  <div class="rule" style="left:21px;top:70px;width:60px"></div>
  <p class="para" style="left:21px;top:74px;width:63px">Short placeholder text describes the study background, the chosen methods and the main clinical findings, written so that colleagues and family can follow each step. Add results, limitations and notes here once the trial data is final.</p>
  <div class="photo deep" style="left:100px;top:20px;width:138px;height:105px" role="img" aria-label="Black and white photo of a surgeon operating under theatre lights"></div>
  <span class="foot date">Thursday, October 5, 2023</span>
  <span class="foot uni">Brellmoor University - Phd defence - surgical science</span>
  <span class="foot num">24</span>
</section>

</body>
</html>
```